Wine Label for Sparkling Pinot Noir

Design a label for Keloru Sparkling Pinot Noir 2016.
It is a single label with main area and more discreet required wine details on one side (must be readable, see example pdf). All elements are displayed in the example pdf.

Logo is our Thai Lady 'Shield', which can be modified as required (flowers removed, color changed etc). Brand name is 'Keloru'

Label needs to be professional and elegant with a slight Asian influence.

Dimensions of the label are: 130mm wide x 80mm height
SVG final product
Leave a bleed edge around (ie. dont put text right to the edge)
Printing will be 4CP, so can be creative as you like with colors and design.

Do a google for 'Stone in River Sparkling Pinot Noir' for some inspiration!

Target Market(s)

Wine drinkers in middle to upper class Restaurants

Logo Text

Keloru - Sparkling Pinot Noir - 2016

Requirements
Must have
• Elegant & Simple with provided text in example pdf
Nice to have
• We are located in an historical mining area.
• Slight Asian influence through our logo.

```html
<!DOCTYPE html>
<html lang="en">
<head>
<meta charset="utf-8">
<title>Keloru Sparkling Pinot Noir 2016 – Wine Label</title>
<link rel="stylesheet" href="https://fonts.googleapis.com/css2?family=Cinzel:wght@400;700&family=Pinyon+Script&display=swap">
<style>
  :root {
    --label-black: #000000;
    --gold: #d9a520;
    --gold-deep: #8a5a08;
    --gold-light: #f4d35a;
    --script-red: #d0141c;
    --ivory: #ffffff;
  }
  * { margin: 0; padding: 0; box-sizing: border-box; }
  html, body {
    width: 1200px;
    height: 722px;
    overflow: hidden;
    background: var(--label-black);
  }
  .label {
    position: relative;
    width: 1200px;
    height: 722px;
    background: var(--label-black);
    font-family: "Cinzel", "Times New Roman", serif;
  }
  .ornament-band {
    position: absolute;
    left: 0;
    width: 1200px;
    height: 74px;
    background: linear-gradient(90deg, var(--gold-deep), var(--gold-light) 25%, var(--gold) 50%, var(--gold-light) 75%, var(--gold-deep));
    opacity: 0.85;
  }
  .ornament-band--top { top: 0; }
  .ornament-band--bottom { bottom: 0; height: 78px; }
  .gold-rule {
    position: absolute;
    left: 0;
    width: 1200px;
    height: 3px;
    background: var(--gold);
  }
  .gold-rule--top { top: 79px; }
  .gold-rule--bottom { top: 636px; }
  .brand-seal {
    position: absolute;
    left: 500px;
    top: 128px;
  }
  .brand-name {
    position: absolute;
    left: 0;
    width: 1176px;
    top: 318px;
    text-align: center;
    font-weight: 700;
    font-size: 68px;
    letter-spacing: 2px;
    color: var(--gold);
    line-height: 1;
  }
  .style-name {
    position: absolute;
    left: 0;
    width: 1176px;
    top: 398px;
    text-align: center;
    font-family: "Pinyon Script", "Brush Script MT", cursive;
    font-size: 54px;
    color: var(--script-red);
    line-height: 1;
  }
  .variety {
    position: absolute;
    left: 0;
    width: 1176px;
    top: 492px;
    text-align: center;
    font-size: 42px;
    font-weight: 400;
    color: var(--ivory);
    letter-spacing: 1px;
    line-height: 1;
  }
  .vintage {
    position: absolute;
    left: 0;
    width: 1176px;
    top: 566px;
    display: flex;
    justify-content: center;
    align-items: center;
    gap: 14px;
    color: var(--ivory);
    font-size: 25px;
    letter-spacing: 6px;
    line-height: 1;
  }
  .vintage__line {
    width: 68px;
    height: 2px;
    background: var(--ivory);
  }
  .vintage__year { padding-left: 6px; }
</style>
</head>
<body>
  <main class="label">
    <div class="ornament-band ornament-band--top" role="img" aria-label="Gold Thai-style scrollwork border"></div>
    <div class="gold-rule gold-rule--top"></div>

    <svg class="brand-seal" width="176" height="176" viewBox="0 0 176 176" aria-hidden="true">
      <circle cx="88" cy="88" r="83" fill="none" stroke="var(--gold)" stroke-width="7"/>
    </svg>

    <h1 class="brand-name">KELORU</h1>
    <p class="style-name">Sparkling</p>
    <p class="variety">Pinot Noir</p>
    <p class="vintage">
      <span class="vintage__line"></span>
      <span class="vintage__year">2016</span>
      <span class="vintage__line"></span>
    </p>

    <div class="gold-rule gold-rule--bottom"></div>
    <div class="ornament-band ornament-band--bottom" role="img" aria-label="Gold Thai-style scrollwork border"></div>
  </main>
</body>
</html>
```